VQB 2023 Postcard

We need a postcard created for an upcoming trade show. We had something made for our sister company a while back and are interested in a similar look. We have included images and some layouts that can be used along with our logo. We like earthy colors, gray and black are okay too. We would like it to be 5x7 and landscape orientation. We have attached the wording we would like to see on the back of the card with changes made in red.
Target Market(s)
retailers
Industry/Entity Type
wedding ring
Colors
Designer to choose only greyscale colors for use in the design.

```html
<!DOCTYPE html>
<html lang="en">
<head>
<meta charset="utf-8">
<title>VQB 2023 Postcard – Front and Back</title>
<link href="https://fonts.googleapis.com/css2?family=Cormorant+Garamond:wght@500;600&family=Poppins:wght@300;400&display=swap" rel="stylesheet">
<style>
  :root {
    --canvas: #c4c4c4;
    --taupe: #b2a794;
    --stone-mid: #a89c87;
    --stone-deep: #6e5a4c;
    --frame-light: #e6e0d4;
    --ink: #2a2826;
    --heading: #a99d88;
    --body: #3a3836;
    --paper: #fbfaf8;
    --tick: #9a9a9a;
    --metal-light: #dcdcdc;
    --metal-mid: #c9c9c9;
  }
  * { box-sizing: border-box; margin: 0; padding: 0; }
  html, body { width: 931px; height: 1200px; overflow: hidden; }
  body {
    background: var(--canvas);
    font-family: "Poppins", Arial, sans-serif;
    color: var(--body);
    position: relative;
  }
  .postcard {
    position: absolute;
    left: 115px;
    width: 700px;
    height: 500px;
    overflow: hidden;
    box-shadow: 0 6px 14px rgba(0,0,0,.25);
  }
  .postcard--front { top: 60px; background: var(--taupe); }
  .postcard--back { top: 630px; background: var(--paper); }

  .card-frame {
    position: absolute;
    inset: 16px;
    border: 2px solid var(--frame-light);
    pointer-events: none;
    z-index: 3;
  }
  .postcard--back .card-frame { border-color: #ddd6c9; border-width: 3px; }

  /* Front */
  .stone-photo {
    position: absolute;
    inset: 0;
    background: linear-gradient(180deg, var(--taupe) 0%, var(--taupe) 50%, var(--stone-mid) 75%, var(--stone-deep) 100%);
  }
  .front-brand {
    position: absolute;
    top: 38px;
    left: 0; right: 0;
    display: flex;
    flex-direction: column;
    align-items: center;
    gap: 6px;
    z-index: 2;
  }
  .brand-square {
    width: 78px; height: 78px;
    border: 5px solid var(--ink);
  }
  .front-brand .brand-name {
    font-family: "Cormorant Garamond", Georgia, serif;
    font-weight: 500;
    font-size: 20px;
    letter-spacing: 1px;
    color: var(--ink);
    line-height: 1;
  }
  .front-title {
    position: absolute;
    top: 166px;
    left: 0; right: 0;
    text-align: center;
    z-index: 2;
  }
  .front-title .eyebrow {
    font-weight: 300;
    font-size: 21px;
    letter-spacing: 16px;
    color: var(--ink);
    padding-left: 16px;
    line-height: 1.3;
  }
  .front-title .headline {
    font-family: "Cormorant Garamond", Georgia, serif;
    font-weight: 600;
    font-size: 47px;
    line-height: 1;
    color: #fff;
    margin-top: 2px;
  }

  /* Back */
  .back-content {
    position: absolute;
    top: 42px;
    left: 43px;
    width: 390px;
    z-index: 2;
  }
  .section-title {
    font-family: "Cormorant Garamond", Georgia, serif;
    font-weight: 600;
    font-size: 23px;
    color: var(--heading);
    line-height: 1.1;
  }
  .section-sub {
    font-size: 10px;
    color: var(--body);
    margin-top: 2px;
    white-space: nowrap;
  }
  .tick-list {
    list-style: none;
    font-size: 10.5px;
    color: var(--body);
  }
  .tick-list li {
    display: flex;
    align-items: center;
    gap: 5px;
    height: 21px;
    white-space: nowrap;
  }
  .tick-list svg { width: 10px; height: 10px; flex: none; }
  .program-list { margin-top: 14px; }
  .trusted { margin-top: 26px; }
  .trusted-grid {
    display: grid;
    grid-template-columns: 200px 190px;
    margin-top: 6px;
  }
  .back-contact {
    position: absolute;
    left: 48px;
    bottom: 36px;
    display: flex;
    align-items: stretch;
    z-index: 2;
  }
  .contact-brand {
    display: flex;
    flex-direction: column;
    align-items: center;
    gap: 3px;
    width: 74px;
  }
  .contact-brand .brand-square {
    width: 60px; height: 52px;
    border: 4px solid var(--heading);
  }
  .contact-brand .brand-name {
    font-family: "Cormorant Garamond", Georgia, serif;
    font-weight: 500;
    font-size: 13px;
    color: var(--heading);
  }
  .contact-divider {
    width: 1px;
    background: #d8d2c6;
    margin: 0 18px;
  }
  .contact-details { padding-top: 2px; }
  .contact-label {
    font-size: 9.5px;
    color: var(--heading);
  }
  .contact-line {
    display: flex;
    align-items: flex-start;
    gap: 3px;
    font-size: 13px;
    color: var(--body);
    line-height: 1.2;
    margin-top: 4px;
  }
  .contact-line svg { width: 11px; height: 11px; margin-top: 2px; flex: none; }
  .ring-stack-photo {
    position: absolute;
    right: 48px;
    top: 44px;
    width: 210px;
    height: 430px;
    background: linear-gradient(180deg, var(--metal-light) 0%, var(--metal-mid) 100%);
    z-index: 1;
  }
</style>
</head>
<body>

  <section class="postcard postcard--front" aria-label="Postcard front">
    <div class="stone-photo" role="img" aria-label="Photograph of wedding bands in white, two-tone and yellow gold resting on a textured stone surface"></div>
    <div class="card-frame"></div>
    <div class="front-brand">
      <div class="brand-square"></div>
      <div class="brand-name">EVERMORE BANDS</div>
    </div>
    <div class="front-title">
      <div class="eyebrow">PREMIUM</div>
      <div class="headline">CUSTOMIZED PROGRAMS</div>
    </div>
  </section>

  <section class="postcard postcard--back" aria-label="Postcard back">
    <div class="card-frame"></div>
    <div class="ring-stack-photo" role="img" aria-label="Photograph of a balanced stack of wedding bands in white, rose and yellow gold"></div>

    <div class="back-content">
      <h2 class="section-title">PREMIUM CUSTOMIZED PROGRAMS</h2>
      <p class="section-sub">PROMOTE YOUR OWN BRAND RINGS STAMPED WITH YOUR SPECIFIED LOGO</p>
      <ul class="tick-list program-list">
        <li><svg viewBox="0 0 10 10"><circle cx="5" cy="5" r="4.3" fill="none" stroke="var(--tick)" stroke-width=".8"/><path d="M3 5.1l1.4 1.4L7.1 3.8" fill="none" stroke="var(--tick)" stroke-width=".9"/></svg>Offer rings in any width, 3 thickness and all precious metals</li>
        <li><svg viewBox="0 0 10 10"><circle cx="5" cy="5" r="4.3" fill="none" stroke="var(--tick)" stroke-width=".8"/><path d="M3 5.1l1.4 1.4L7.1 3.8" fill="none" stroke="var(--tick)" stroke-width=".9"/></svg>Combine &amp; customize 5500 ring designs</li>
        <li><svg viewBox="0 0 10 10"><circle cx="5" cy="5" r="4.3" fill="none" stroke="var(--tick)" stroke-width=".8"/><path d="M3 5.1l1.4 1.4L7.1 3.8" fill="none" stroke="var(--tick)" stroke-width=".9"/></svg>Sell in platinum, 18kt, 14kt &amp; 10kt</li>
        <li><svg viewBox="0 0 10 10"><circle cx="5" cy="5" r="4.3" fill="none" stroke="var(--tick)" stroke-width=".8"/><path d="M3 5.1l1.4 1.4L7.1 3.8" fill="none" stroke="var(--tick)" stroke-width=".9"/></svg>Samples kits starting as low as $900</li>
        <li><svg viewBox="0 0 10 10"><circle cx="5" cy="5" r="4.3" fill="none" stroke="var(--tick)" stroke-width=".8"/><path d="M3 5.1l1.4 1.4L7.1 3.8" fill="none" stroke="var(--tick)" stroke-width=".9"/></svg>Program performance money back guarantee</li>
      </ul>

      <h2 class="section-title trusted">YOUR TRUSTED SOURCE FOR RINGS</h2>
      <div class="trusted-grid">
        <ul class="tick-list">
          <li><svg viewBox="0 0 10 10"><circle cx="5" cy="5" r="4.3" fill="none" stroke="var(--tick)" stroke-width=".8"/><path d="M3 5.1l1.4 1.4L7.1 3.8" fill="none" stroke="var(--tick)" stroke-width=".9"/></svg>Easy pricing system</li>
          <li><svg viewBox="0 0 10 10"><circle cx="5" cy="5" r="4.3" fill="none" stroke="var(--tick)" stroke-width=".8"/><path d="M3 5.1l1.4 1.4L7.1 3.8" fill="none" stroke="var(--tick)" stroke-width=".9"/></svg>Scrap buyout options</li>
          <li><svg viewBox="0 0 10 10"><circle cx="5" cy="5" r="4.3" fill="none" stroke="var(--tick)" stroke-width=".8"/><path d="M3 5.1l1.4 1.4L7.1 3.8" fill="none" stroke="var(--tick)" stroke-width=".9"/></svg>1 week turnaround</li>
          <li><svg viewBox="0 0 10 10"><circle cx="5" cy="5" r="4.3" fill="none" stroke="var(--tick)" stroke-width=".8"/><path d="M3 5.1l1.4 1.4L7.1 3.8" fill="none" stroke="var(--tick)" stroke-width=".9"/></svg>family owned and operated</li>
        </ul>
        <ul class="tick-list">
          <li><svg viewBox="0 0 10 10"><circle cx="5" cy="5" r="4.3" fill="none" stroke="var(--tick)" stroke-width=".8"/><path d="M3 5.1l1.4 1.4L7.1 3.8" fill="none" stroke="var(--tick)" stroke-width=".9"/></svg>Free shipping</li>
          <li><svg viewBox="0 0 10 10"><circle cx="5" cy="5" r="4.3" fill="none" stroke="var(--tick)" stroke-width=".8"/><path d="M3 5.1l1.4 1.4L7.1 3.8" fill="none" stroke="var(--tick)" stroke-width=".9"/></svg>Pre-tagged samples</li>
          <li><svg viewBox="0 0 10 10"><circle cx="5" cy="5" r="4.3" fill="none" stroke="var(--tick)" stroke-width=".8"/><path d="M3 5.1l1.4 1.4L7.1 3.8" fill="none" stroke="var(--tick)" stroke-width=".9"/></svg>Competitive pricing</li>
          <li><svg viewBox="0 0 10 10"><circle cx="5" cy="5" r="4.3" fill="none" stroke="var(--tick)" stroke-width=".8"/><path d="M3 5.1l1.4 1.4L7.1 3.8" fill="none" stroke="var(--tick)" stroke-width=".9"/></svg>Made proudly in the usa</li>
        </ul>
      </div>
    </div>

    <div class="back-contact">
      <div class="contact-brand">
        <div class="brand-square"></div>
        <div class="brand-name">EVERMORE</div>
      </div>
      <div class="contact-divider"></div>
      <div class="contact-details">
        <p class="contact-label">CONTACT US FOR MORE INFORMATION</p>
        <p class="contact-line"><svg viewBox="0 0 12 12"><path d="M3 1.5l1.6 2.2-.9 1.1c.6 1.3 1.5 2.2 2.8 2.8l1.1-.9 2.2 1.6-.8 1.7C5.5 10 2 6.5 1.3 2.3z" fill="none" stroke="var(--tick)" stroke-width=".9"/></svg>800-555-0142</p>
        <p class="contact-line"><svg viewBox="0 0 12 12"><path d="M6 11S2.2 7 2.2 4.6a3.8 3.8 0 017.6 0C9.8 7 6 11 6 11z" fill="none" stroke="var(--tick)" stroke-width=".9"/><circle cx="6" cy="4.6" r="1.3" fill="none" stroke="var(--tick)" stroke-width=".9"/></svg><span>140 Meadowbrook Lane, Glen Harbor<br>NY 11000</span></p>
      </div>
    </div>
  </section>

</body>
</html>
```